Simple, Professional and neat business card design for Vendralo Inc.

We're looking to re-vamp our business card design. We're a supplier of innovative feed ingredients for the North American animal agriculture industry. We are located in Lucknow, Ontario, Canada and our flagship product is a product that prevents milk fever in dairy cows when the calve, it is fed before calving and is very effective compared to other alternatives available on the market today.

Our company has Danish roots and we import all of our product from our Danish partner/manufacturer in Denmark. We like our design to embrace high professionalism while remaining neat and simple.

Target Market(s)

B2B, Feed Mills, Veterinary Clinics, Large integrators/producers,

Industry/Entity Type

Agribusiness

Contact Information for Business Card

We like the rounded corners because they make the card easy to sit in a wallet and not many use it so it makes the card stand out, just possibly something to take account for during the design.

As you can also see on the sliders below, looking for a that simple but proffesional scandinavian design.

Requirements
Nice to have
• Rounded corners
Should not have
• Too vibrant

```html
<!DOCTYPE html>
<html lang="en">
<head>
<meta charset="utf-8">
<title>Vendralo Inc. Business Card</title>
<link href="https://fonts.googleapis.com/css2?family=Lato:wght@400;700&display=swap" rel="stylesheet">
<style>
  :root {
    --page-bg: #e9ebee;
    --brand-blue: #2f75c4;
    --brand-blue-light: #5e9fdc;
    --brand-blue-dark: #1f63b3;
    --swoosh-grey: #8a8c90;
    --ink: #222428;
    --paper: #ffffff;
  }
  * { box-sizing: border-box; margin: 0; padding: 0; }
  html, body {
    width: 1200px; height: 900px; overflow: hidden;
    background: var(--page-bg);
    font-family: "Lato", Arial, sans-serif;
  }
  .canvas { position: relative; width: 1200px; height: 900px; }
  .card {
    position: absolute;
    width: 640px; height: 366px;
    border-radius: 22px;
    overflow: hidden;
    box-shadow: 0 10px 28px rgba(0,0,0,0.18);
  }
  /* Back side */
  .card-back {
    left: 120px; top: 60px;
    background: linear-gradient(160deg, var(--brand-blue-light) 0%, var(--brand-blue) 55%, var(--brand-blue-dark) 100%);
  }
  .back-mark {
    position: absolute; left: 0; right: 0; top: 118px;
    display: flex; align-items: center; justify-content: center; gap: 16px;
  }
  .back-mark .dot { width: 46px; height: 46px; border-radius: 50%; background: var(--paper); }
  .back-mark .name { color: var(--paper); font-weight: 700; font-size: 44px; letter-spacing: 3px; }
  .back-web {
    position: absolute; left: 0; right: 0; top: 228px;
    text-align: center; color: var(--paper);
    font-size: 13px; font-weight: 700; letter-spacing: 7px;
  }
  /* Front side */
  .card-front { left: 440px; top: 474px; background: var(--paper); }
  .front-swoosh { position: absolute; inset: 0; }
  .company {
    position: absolute; left: 130px; top: 50px;
    display: flex; align-items: center; gap: 14px;
  }
  .company .dot { width: 38px; height: 38px; border-radius: 50%; background: var(--brand-blue); }
  .company .name { color: var(--brand-blue); font-weight: 700; font-size: 32px; letter-spacing: 1px; white-space: nowrap; }
  .person { position: absolute; right: 56px; top: 112px; }
  .person .full-name { color: var(--brand-blue); font-weight: 700; font-size: 16px; letter-spacing: 0.5px; }
  .person .role { color: var(--ink); font-size: 12px; margin-top: 2px; padding-left: 40px; }
  .person .email { color: var(--brand-blue); font-weight: 700; font-size: 13px; margin-top: 16px; padding-left: 40px; }
  .contacts {
    position: absolute; left: 52px; top: 206px;
    display: grid; grid-template-columns: auto auto; column-gap: 12px; row-gap: 6px;
    font-size: 13px;
  }
  .contacts dt {
    color: var(--brand-blue); font-weight: 700;
    border-bottom: 1px solid var(--brand-blue-light); padding-bottom: 1px;
  }
  .contacts dd { color: var(--ink); }
</style>
</head>
<body>
<main class="canvas">
  <section class="card card-back" aria-label="Card back">
    <div class="back-mark">
      <span class="dot"></span>
      <span class="name">VENDRALO</span>
    </div>
    <p class="back-web">www.vendralo.com</p>
  </section>

  <section class="card card-front" aria-label="Card front">
    <svg class="front-swoosh" viewBox="0 0 640 366" width="640" height="366" aria-hidden="true">
      <path d="M290 338 C430 318 560 270 640 196 V214 C560 282 440 324 290 338 Z" fill="var(--swoosh-grey)"/>
      <path d="M0 366 V344 C300 338 520 292 640 222 V366 Z" fill="var(--brand-blue)"/>
    </svg>

    <div class="company">
      <span class="dot"></span>
      <span class="name">VENDRALO INC.</span>
    </div>

    <div class="person">
      <p class="full-name">MIKKEL SØRHAVEN</p>
      <p class="role">Managing Director</p>
      <p class="email">mikkel@vendralo.com</p>
    </div>

    <dl class="contacts">
      <dt>Mobile:</dt><dd>555-014-0333</dd>
      <dt>Office:</dt><dd>555-014-5822</dd>
      <dt>Fax:</dt><dd>555-014-5999</dd>
      <dt>Toll Free:</dt><dd>888-555-0147</dd>
    </dl>
  </section>
</main>
</body>
</html>
```